Harvest Bridge Brochure Design Project

We need a brochure that we can use to promote our education not-for-profit, Harvest Bridge Fund (www.harvestbridgeco.com) and promote our African bracelets that we are selling to fundraise for our organisation. The target audience is from high school to 40 years in the US and Australia.
Updates

Please find below the link to a new hi res logo. Thanks!
https://www.filecrate.net/s/9qm27vtrw84hzpa/Harvest_Bridge_logo_NEW.ai
https://www.filecrate.net/sh/3kd8wrx51bq2ve7/QPMNZRfo7Y

Reason: We have decided the final design to choose. Please give us a week to finalise.

Industry/Entity Type

High School

Requirements
Must have
• Photos of bracelets
Harvest Bridge logo
emotive photos of African students
A4 size with fold out features

```html
<!DOCTYPE html>
<html lang="en">
<head>
<meta charset="utf-8">
<title>Harvest Bridge Brochure – Inside Spread</title>
<link href="https://fonts.googleapis.com/css2?family=Oswald:wght@500&family=Roboto:wght@400;700&display=swap" rel="stylesheet">
<style>
  :root{
    --page:#ffffff;
    --paper:#fcf2e3;
    --ink:#1e1e1e;
    --orange:#e0704a;
    --yellow:#f3b52a;
    --lemon:#f8ec54;
    --red:#d9202e;
    --fold:#cfc6b8;
    --dash:#e0333a;
    --dash-gold:#c98a3a;
  }
  *{box-sizing:border-box;margin:0;padding:0}
  html,body{width:1200px;height:1000px;overflow:hidden;background:var(--page)}
  body{position:relative;font-family:"Roboto",Arial,sans-serif;color:var(--ink)}

  .panel-label{position:absolute;top:55px;width:200px;text-align:center;font:400 14px/16px "Roboto",Arial,sans-serif;letter-spacing:.3px;text-transform:uppercase}

  .spread{position:absolute;left:20px;top:91px;width:1162px;height:821px;background:var(--paper);overflow:hidden;box-shadow:2px 3px 6px rgba(0,0,0,.18)}
  .band{position:absolute;left:0;width:1162px;display:block}
  .band--top{top:0}
  .band--bottom{bottom:0}
  .fold{position:absolute;top:0;bottom:0;border-left:1px dotted var(--fold)}

  .tag{position:absolute;font:500 17px/1 "Oswald",sans-serif;letter-spacing:.5px;padding:9px 14px 9px 12px;text-transform:uppercase;color:var(--ink)}
  .tag--orange{background:var(--orange)}
  .tag--lemon{background:var(--lemon)}

  .copy{position:absolute;font-size:12.4px;line-height:18px}
  .copy p+p{margin-top:10px}

  .photo{position:absolute}
  .photo--class{left:38px;top:478px;width:314px;height:236px;border:6px solid #fff;transform:rotate(-0.6deg);box-shadow:1px 3px 6px rgba(0,0,0,.3);background:linear-gradient(180deg,#b9c4b6 0%,#8c8f70 40%,#4c4a3a 100%)}
  .photo--student{left:352px;top:364px;width:426px;height:457px;border-radius:150px 170px 0 0;background:linear-gradient(180deg,#6b5548 0%,#86817c 45%,#8d8c8a 100%)}
  .photo--bracelet{border-radius:6px}
  .photo--bracelet-single{left:858px;top:150px;width:150px;height:110px;background:linear-gradient(135deg,#e3b08a 0%,#c98554 100%)}
  .photo--bracelet-pair{left:812px;top:280px;width:312px;height:110px;background:linear-gradient(135deg,#5a514a 0%,#2f2a26 100%)}

  .frame{position:absolute;border:1px dashed var(--dash)}
  .frame--top{left:850px;top:130px;width:147px;height:140px}
  .frame--bottom{left:850px;top:269px;width:214px;height:163px;border-top-color:var(--dash-gold);border-right-color:var(--dash-gold)}

  .help{position:absolute;left:817px;top:527px;width:340px;font-size:12.4px;line-height:18px}
  .help__lead{font-weight:700;font-size:14px;line-height:16px;text-transform:uppercase;letter-spacing:.2px}
  .help__list{list-style:none;margin:8px 0 0 -4px}
  .help__list li{display:flex;align-items:center;gap:6px;height:26px}
  .num{display:inline-flex;align-items:center;justify-content:center;width:17px;height:17px;border-radius:50%;background:#111;color:#fff;font-weight:700;font-size:11px}
  .help__or{font-weight:700;margin-top:3px}
  .help__donate{margin-top:8px}
</style>
</head>
<body>
  <div class="panel-label" style="left:112px">Inside Left</div>
  <div class="panel-label" style="left:497px">Inside Centre</div>
  <div class="panel-label" style="left:884px">Inside Right</div>

  <main class="spread">
    <svg class="band band--top" height="64" viewBox="0 0 1162 64" role="img" aria-label="Spotted animal-print border in orange, yellow and red">
      <defs>
        <linearGradient id="bandTone" x1="0" x2="1" y1="0" y2="0">
          <stop offset="0" stop-color="#f2b43a"/><stop offset=".3" stop-color="#ec7a2a"/>
          <stop offset=".5" stop-color="#dc2a2e"/><stop offset=".7" stop-color="#ec7a2a"/>
          <stop offset="1" stop-color="#f2b43a"/>
        </linearGradient>
      </defs>
      <path d="M0 0H1162V58q-20 6 -40 0t-40 0t-40 0t-40 0t-40 0t-40 0t-40 0t-40 0t-40 0t-40 0t-40 0t-40 0t-40 0t-40 0t-40 0t-40 0t-40 0t-40 0t-40 0t-40 0t-40 0t-40 0t-40 0t-40 0t-40 0t-40 0t-40 0t-40 0t-40 0L0 58Z" fill="url(#bandTone)" opacity=".85"/>
    </svg>
    <svg class="band band--bottom" height="56" viewBox="0 0 1162 56" role="img" aria-label="Spotted animal-print border in orange, yellow and red">
      <path d="M0 6q20 -6 40 0t40 0t40 0t40 0t40 0t40 0t40 0t40 0t40 0t40 0t40 0t40 0t40 0t40 0t40 0t40 0t40 0t40 0t40 0t40 0t40 0t40 0t40 0t40 0t40 0t40 0t40 0t40 0t40 0L1162 6V56H0Z" fill="url(#bandTone)" opacity=".85"/>
    </svg>

    <div class="fold" style="left:390px"></div>
    <div class="fold" style="left:778px"></div>

    <section class="panel panel--left">
      <h2 class="tag tag--orange" style="left:27px;top:121px">Our Philosophy</h2>
      <div class="copy" style="left:39px;top:173px;width:305px">
        <p>We subscribe to the philosophy of development through education – the idea that education is the most powerful and effective way to bring change, independence, innovation, and prosperity. Fundamentally, the belief is that education can serve towards ending aspects of poverty, bringing enlightenment, and transforming individual lives and communities.</p>
        <p>Harvest Bridge strives to be part of the effort to create the next generation of educated African who are independent thinkers and innovators. We aim to instill the spirit of giving back within the students and ensure that they will contribute to the future growth and prosperity of Zimbabwe and Africa at large.</p>
      </div>
      <div class="photo photo--class" role="img" aria-label="Photo of a teacher with a class of uniformed students seated outdoors under trees"></div>
    </section>

    <section class="panel panel--centre">
      <h2 class="tag tag--lemon" style="left:412px;top:118px">The Need</h2>
      <div class="copy" style="left:430px;top:173px;width:310px">
        <p>For every student we have helped, we have turned down at least five other motivated, intelligent and desperate students who we cannot help due financial constraints. We more of our students are finishing high school and graduating from our program, we reaching out to our supporters to help us recruit more students into the Harvest Bridge Scholarship Program and give them and their families a chance at life.</p>
      </div>
      <div class="photo photo--student" role="img" aria-label="Photo of a smiling young schoolboy in a grey jumper and white collar, flexing one arm"></div>
    </section>

    <section class="panel panel--right">
      <div class="photo photo--bracelet photo--bracelet-single" role="img" aria-label="Photo of a tan leather snap bracelet with beaded accents"></div>
      <div class="photo photo--bracelet photo--bracelet-pair" role="img" aria-label="Photo of two dark leather snap bracelets"></div>
      <div class="frame frame--top"></div>
      <div class="frame frame--bottom"></div>

      <h2 class="tag tag--orange" style="left:803px;top:481px">How You Can Help</h2>
      <div class="help">
        <p class="help__lead">Buy, Sell or Promote</p>
        <p>the Harvest Bridge Bracelets.</p>
        <ul class="help__list">
          <li><span class="num">1</span>bracelet = One Month of school for one child</li>
          <li><span class="num">3</span>bracelets = One Term of school for one child</li>
          <li><span class="num">9</span>bracelets = one year of school for one child</li>
        </ul>
        <p class="help__or">OR</p>
        <p class="help__donate">Donate to Harvest Bridge Fund at<br>www.harvestbridgeco.com</p>
      </div>
    </section>
  </main>
</body>
</html>
```